Brivoza banner and eDM design

We need banner ads and an eDM header to promote Brivoza.com.au (not currently live but logo and site design complete).

Banners should ideally be in flash with back-up gifs but we would be open to just animated gifs as well.

Banner sizes to be delivered are:
300x250
729x90
468x60
160x600

Best to keep banner file size under 25kb if possible (based on standard publisher specs)

For the eDM header, it should be around:
600 wide x
150-200 high

The advertising role is to promote the websites services which are related to making HR easy for small business owners - specifically relating to recruitment, induction, engagement and employee exit. I'll attach more details on this.

Target Market(s)

Small and medium business owners - slightly male skew

Industry/Entity Type

Small Business

Requirements
Must have
• Must match the look and feel and colour palette of the logo and website design that will be attached to this brief.

Must look professional

Must follow the copy guide for the frames as outlined in the attachment - there are 2 options for frame 3 listed. I'd like to get 2 sets of banners developed to cover both options.

Must have clear call-to-action
Nice to have
• Nice to have sophisticated animation if possible

I've added two potential images that could be used - either could be used to illustrate the 'Save time and improve results' line -
one focused on finding the right person
one is focused on improving results through a team

You could potentially use a screen grab of the site homepage in the design too - but only if eligible since none of the copy on it is finalised.

```html
<!DOCTYPE html>
<html lang="en">
<head>
<meta charset="utf-8">
<title>Brivoza banner</title>
<link href="https://fonts.googleapis.com/css2?family=Arimo:wght@400;700&display=swap" rel="stylesheet">
<style>
  :root {
    --panel-dark: #0d3a86;
    --panel-mid: #1f5bb5;
    --panel-light: #2f73cc;
    --chevron: #dfe5ee;
    --brand-blue: #1d58b0;
    --text-dark: #333333;
    --cta-top: #ff8a1e;
    --cta-bottom: #e85d00;
    --white: #ffffff;
    --art-light: #eef5fb;
    --art-mid: #9cc9ea;
  }
  html, body {
    margin: 0;
    padding: 0;
    overflow: hidden;
    background: var(--white);
  }
  .banner {
    position: relative;
    width: 1200px;
    height: 148px;
    overflow: hidden;
    background: var(--white);
    font-family: "Arimo", Arial, sans-serif;
  }
  .hero-art {
    position: absolute;
    left: 0;
    top: 0;
    width: 390px;
    height: 148px;
    background: linear-gradient(90deg, var(--art-mid) 0%, var(--art-light) 55%, var(--art-mid) 100%);
  }
  .message-panel {
    position: absolute;
    left: 370px;
    top: 0;
    width: 450px;
    height: 148px;
  }
  .headline,
  .subline {
    position: absolute;
    left: 438px;
    margin: 0;
    color: var(--white);
    white-space: nowrap;
  }
  .headline {
    top: 28px;
    font-size: 44px;
    font-weight: 700;
    letter-spacing: -0.5px;
  }
  .subline {
    top: 88px;
    left: 418px;
    font-size: 31px;
    font-weight: 400;
  }
  .brand {
    position: absolute;
    left: 838px;
    top: 12px;
    display: flex;
    align-items: center;
    gap: 10px;
  }
  .brand-dot {
    width: 36px;
    height: 36px;
    border-radius: 50%;
    background: var(--brand-blue);
  }
  .brand-name {
    font-size: 42px;
    font-weight: 700;
    color: var(--brand-blue);
    line-height: 1;
  }
  .tagline {
    position: absolute;
    left: 838px;
    top: 64px;
    margin: 0;
    font-size: 19px;
    font-weight: 700;
    color: var(--text-dark);
    white-space: nowrap;
  }
  .cta {
    position: absolute;
    left: 895px;
    top: 94px;
    width: 224px;
    height: 44px;
    display: flex;
    align-items: center;
    justify-content: center;
    background: linear-gradient(180deg, var(--cta-top), var(--cta-bottom));
    color: var(--white);
    font-size: 23px;
    font-weight: 700;
    text-decoration: none;
    border: 1px solid #c94f00;
  }
</style>
</head>
<body>
  <div class="banner">
    <div class="hero-art" role="img" aria-label="Crowd of blue figures with a magnifying glass highlighting one orange person"></div>

    <svg class="message-panel" viewBox="0 0 450 148" aria-hidden="true">
      <defs>
        <linearGradient id="panelFill" x1="0" y1="0" x2="1" y2="1">
          <stop offset="0" stop-color="var(--panel-light)"/>
          <stop offset="0.5" stop-color="var(--panel-mid)"/>
          <stop offset="1" stop-color="var(--panel-dark)"/>
        </linearGradient>
      </defs>
      <polygon points="0,0 30,0 68,74 30,148 0,148 38,74" fill="var(--chevron)"/>
      <polygon points="30,0 450,0 450,148 30,148 68,74" fill="url(#panelFill)"/>
    </svg>

    <p class="headline">Save Time</p>
    <p class="subline">and improve results</p>

    <div class="brand">
      <span class="brand-dot"></span>
      <span class="brand-name">Brivoza</span>
    </div>
    <p class="tagline">Easy end to end HR solutions</p>
    <a class="cta" href="#">Find out more</a>
  </div>
</body>
</html>
```